TL Estates
Desmond Parkes
TL Estates - Real Estate
Creative Brief
Corporate
Owner/ Realtor
Suite # 17 Ashbury Business Centre, 28 Calder Rd. Kingston 5
dp@desmondparkes-example.com
www.desmondparkes-example.com
Business card , Letter head and envelopes to compliment LOGO i DO NOT WANT MY PICTURE TO APPEAR IN A BOX...I WOULD WANT IT TO BE FLOATING ON THE BUSINESS CARD I would like for the designers to colour my shirt RED

```html
<!DOCTYPE html>
<html lang="en">
<head>
<meta charset="utf-8">
<title>TL Estates – Business Cards</title>
<link href="https://fonts.googleapis.com/css2?family=Arimo:wght@400;700&display=swap" rel="stylesheet">
<style>
:root{
  --bg:#d9dadc;
  --card:#ffffff;
  --red:#c8141c;
  --red-dark:#8e0b10;
  --grey:#d4d6d8;
  --grey-dark:#9a9ea2;
  --ink:#3a3a3a;
  --muted:#6b6b6b;
}
*{margin:0;padding:0;box-sizing:border-box}
html,body{width:1200px;height:689px;overflow:hidden}
body{background:var(--bg);font-family:"Arimo",Arial,sans-serif;color:var(--ink);position:relative}
.card{position:absolute;background:var(--card);border-radius:18px;overflow:hidden;box-shadow:0 4px 10px rgba(0,0,0,.25)}
.card svg.wave{position:absolute;left:0;bottom:0;width:100%}
.brand{position:absolute;display:flex;flex-direction:column;align-items:center}
.brand-mark{width:58px;height:58px;background:linear-gradient(180deg,var(--red),var(--red-dark));border-radius:3px}
.brand-name{margin-top:8px;font-weight:700;font-size:26px;color:var(--red);white-space:nowrap}
.brand-tag{margin-top:3px;font-size:9px;letter-spacing:1.5px;color:var(--muted);white-space:nowrap}
.portrait{position:absolute;background:radial-gradient(ellipse at 50% 30%,#8a5a44 0%,#6d4333 35%,#d53a2a 60%,#e95a3c 100%);border-radius:45% 45% 8px 8px}
.person{position:absolute;text-align:right;white-space:nowrap}
.person .name{font-weight:700;font-size:17px;color:#222}
.person .role{font-size:13px;color:var(--muted);margin-top:2px}
.address{position:absolute;font-size:12px;line-height:17px;color:var(--ink);white-space:nowrap}
.contacts{position:absolute;font-size:12px;line-height:18px;list-style:none;white-space:nowrap}
.contacts.compact{font-size:11px}
.contacts li{display:flex;align-items:center;gap:6px}
.contacts svg{width:9px;height:9px;fill:var(--red)}
.web{position:absolute;font-weight:700;font-size:13px;color:#fff;white-space:nowrap}
.web.red{color:var(--red)}
.badge{position:absolute;background:#fff;border:1px solid #999;border-radius:2px}
.badge.dark{background:#333;border-color:#333}
.divider{position:absolute;width:1px;background:var(--grey-dark)}
.strip{position:absolute;left:0;right:0;bottom:0;height:32px;background:linear-gradient(180deg,var(--red),var(--red-dark))}
</style>
</head>
<body>

<!-- Front card, style A -->
<section class="card" style="left:29px;top:24px;width:487px;height:295px">
  <div class="brand" style="left:26px;top:18px">
    <div class="brand-mark"></div>
    <div class="brand-name">TL Estates</div>
    <div class="brand-tag">REAL ESTATE. REAL PEOPLE</div>
  </div>
  <div class="portrait" role="img" aria-label="Photo of Desmond Parkes in a red shirt, floating cut-out" style="left:300px;top:10px;width:140px;height:168px"></div>
  <div class="person" style="right:40px;top:180px">
    <div class="name">Desmond Parkes</div>
    <div class="role">Owner/ Realtor</div>
  </div>
  <div class="address" style="left:20px;top:134px">Suite # 17, Ashbury Business Centre<br>28 Calder Rd. Kingston 5</div>
  <ul class="contacts" style="left:20px;top:176px">
    <li><svg viewBox="0 0 10 10"><circle cx="5" cy="5" r="4"/></svg>876-555-0142 &nbsp; <svg viewBox="0 0 10 10"><circle cx="5" cy="5" r="4"/></svg>876-555-0163</li>
    <li><svg viewBox="0 0 10 10"><circle cx="5" cy="5" r="4"/></svg>876-555-0187</li>
    <li><svg viewBox="0 0 10 10"><circle cx="5" cy="5" r="4"/></svg>dp@desmondparkes-example.com</li>
  </ul>
  <svg class="wave" viewBox="0 0 487 80" height="80" preserveAspectRatio="none">
    <path d="M0 30 Q200 70 487 12 L487 80 L0 80Z" fill="var(--grey)"/>
    <path d="M0 48 Q220 78 487 34 L487 80 L0 80Z" fill="var(--red)"/>
  </svg>
  <div class="badge" style="left:340px;top:262px;width:20px;height:20px"></div>
  <div class="badge" style="left:364px;top:264px;width:48px;height:16px"></div>
  <div class="web" style="left:20px;top:270px">www.desmondparkes-example.com</div>
</section>

<!-- Back card, style A -->
<section class="card" style="left:533px;top:24px;width:499px;height:295px">
  <div class="brand" style="left:0;right:0;top:56px">
    <div class="brand-mark"></div>
    <div class="brand-name">TL Estates</div>
    <div class="brand-tag">REAL ESTATE. REAL PEOPLE</div>
  </div>
  <svg class="wave" viewBox="0 0 499 90" height="90" preserveAspectRatio="none">
    <path d="M0 50 Q250 0 499 40 L499 90 L0 90Z" fill="var(--grey)"/>
    <path d="M0 62 Q260 20 499 58 L499 90 L0 90Z" fill="var(--red)"/>
  </svg>
  <div class="web" style="right:28px;top:256px">www.desmondparkes-example.com</div>
</section>

<!-- Front card, style B -->
<section class="card" style="left:29px;top:360px;width:559px;height:293px">
  <div class="brand" style="left:30px;top:22px">
    <div class="brand-mark"></div>
    <div class="brand-name">TL Estates</div>
    <div class="brand-tag">REAL ESTATE. REAL PEOPLE</div>
  </div>
  <div class="badge" style="left:300px;top:28px;width:22px;height:22px"></div>
  <div class="badge dark" style="left:326px;top:32px;width:50px;height:16px"></div>
  <div class="address" style="left:30px;top:150px">Suite # 17<br>Ashbury Business Centre<br>28 Calder Rd. Kingston 5</div>
  <div class="divider" style="left:200px;top:140px;height:92px"></div>
  <ul class="contacts compact" style="left:210px;top:146px">
    <li><svg viewBox="0 0 10 10"><circle cx="5" cy="5" r="4"/></svg>876-555-0142</li>
    <li><svg viewBox="0 0 10 10"><circle cx="5" cy="5" r="4"/></svg>876-555-0187</li>
    <li><svg viewBox="0 0 10 10"><circle cx="5" cy="5" r="4"/></svg>876-555-0163</li>
    <li><svg viewBox="0 0 10 10"><circle cx="5" cy="5" r="4"/></svg>dp@desmondparkes-example.com</li>
  </ul>
  <div class="portrait" role="img" aria-label="Photo of Desmond Parkes in a red shirt, floating cut-out" style="left:410px;top:30px;width:130px;height:188px"></div>
  <div class="person" style="right:24px;top:222px">
    <div class="name">Desmond Parkes</div>
    <div class="role">Owner/ Realtor</div>
  </div>
  <div class="strip"></div>
  <div class="web" style="left:24px;top:270px">www.desmondparkes-example.com</div>
</section>

<!-- Back card, style B -->
<section class="card" style="left:629px;top:360px;width:547px;height:293px">
  <div class="brand" style="left:0;right:0;top:70px">
    <div class="brand-mark"></div>
    <div class="brand-name">TL Estates</div>
    <div class="brand-tag">REAL ESTATE. REAL PEOPLE</div>
  </div>
  <div class="web red" style="left:0;right:0;top:186px;text-align:center">www.desmondparkes-example.com</div>
</section>

</body>
</html>
```